Harborline Frame Construction Needs business card

Hey we are in need of business card designs. I have upload our logo as a guideline, but free feel to run with it or come up with something unique.
Pls have fun with it and be creative. the name says it all!
i will give some directions after i see a few entries..
Logo source file has been uploaded..
Hey because of the logo is so colourful already.
Can we have a few submissions with less colour.
Also we are looking for clever/hidden/descriptive business card.

```html
<!DOCTYPE html>
<html lang="en">
<head>
<meta charset="utf-8">
<title>Harborline Frame Construction – Business Card</title>
<link href="https://fonts.googleapis.com/css2?family=Lato:wght@400;700&display=swap" rel="stylesheet">
<style>
  :root {
    --backdrop: #e9e6e1;
    --card: #ffffff;
    --ink-grey: #77787b;
    --ink-dark: #6d6e70;
    --green: #1a9b48;
    --yellow: #f4c400;
    --blue: #1b8fd6;
    --red: #e2262b;
    --black: #222222;
  }
  * { margin: 0; padding: 0; box-sizing: border-box; }
  html, body {
    width: 1200px; height: 1000px; overflow: hidden;
    background: var(--backdrop);
    font-family: "Lato", Arial, sans-serif;
  }
  .canvas { position: relative; width: 1200px; height: 1000px; }

  .card {
    position: absolute; width: 720px; height: 400px;
    background: var(--card);
    box-shadow: 0 6px 18px rgba(0,0,0,0.18);
    overflow: hidden;
  }
  .card--front { left: 110px; top: 70px; z-index: 2; }
  .card--back  { left: 370px; top: 520px; z-index: 1; }

  /* front */
  .front-brand {
    position: absolute; left: 0; right: 0; top: 140px;
    display: flex; flex-direction: column; align-items: center; gap: 6px;
  }
  .brand-row { display: flex; align-items: center; gap: 16px; white-space: nowrap; }
  .brand-square { width: 34px; height: 34px; background: var(--ink-grey); flex: none; }
  .brand-name {
    font-weight: 700; color: var(--ink-grey);
    font-size: 50px; letter-spacing: 1px; text-transform: uppercase; line-height: 1;
    white-space: nowrap;
  }
  .brand-sub {
    font-weight: 700; color: var(--ink-grey);
    font-size: 18px; letter-spacing: 3px; text-transform: uppercase;
  }

  /* back */
  .back-brand {
    position: absolute; left: 20px; top: 150px; width: 330px;
    display: flex; flex-direction: column; align-items: center; gap: 4px;
  }
  .back-brand .brand-row { gap: 12px; }
  .back-brand .brand-square { width: 20px; height: 20px; }
  .back-brand .brand-name { font-size: 24px; letter-spacing: 0.5px; }
  .back-brand .brand-sub { font-size: 11px; letter-spacing: 2px; }

  .holder { position: absolute; left: 368px; top: 58px; color: var(--ink-grey); }
  .holder-name { font-size: 22px; font-weight: 700; letter-spacing: 1px; text-transform: uppercase; }
  .holder-role { font-size: 16px; letter-spacing: 1px; margin-top: 2px; }

  .contacts { position: absolute; left: 368px; top: 145px; list-style: none; color: var(--ink-dark); }
  .contacts li { display: flex; align-items: center; gap: 12px; font-size: 17px; height: 25px; white-space: nowrap; }
  .contacts svg { width: 15px; height: 15px; flex: none; }

  .address { position: absolute; left: 372px; top: 270px; color: var(--ink-dark); white-space: nowrap; }
  .address-company { font-size: 17px; font-weight: 700; text-transform: uppercase; letter-spacing: 0.2px; }
  .address-line { font-size: 17px; margin-top: 4px; }

  .pattern-band {
    position: absolute; left: 0; right: 0; bottom: 0; height: 34px;
    background: linear-gradient(90deg, var(--green), var(--yellow) 25%, var(--red) 50%, var(--blue) 75%, var(--black));
    opacity: 0.85;
  }
</style>
</head>
<body>
<main class="canvas">

  <section class="card card--front" aria-label="Card front">
    <div class="front-brand">
      <div class="brand-row">
        <span class="brand-square"></span>
        <span class="brand-name">Harborline Frame</span>
      </div>
      <span class="brand-sub">Construction</span>
    </div>
  </section>

  <section class="card card--back" aria-label="Card back">
    <div class="back-brand">
      <div class="brand-row">
        <span class="brand-square"></span>
        <span class="brand-name">Harborline Frame</span>
      </div>
      <span class="brand-sub">Construction</span>
    </div>

    <div class="holder">
      <p class="holder-name">Your Name</p>
      <p class="holder-role">Director</p>
    </div>

    <ul class="contacts">
      <li>
        <svg viewBox="0 0 16 16" aria-hidden="true"><path fill="var(--green)" d="M3 1l3 3-1.5 2a9 9 0 005.5 5.5L12 10l3 3-2 2C7 15 1 9 1 3z"/></svg>
        +1 604 718 3052
      </li>
      <li>
        <svg viewBox="0 0 16 16" aria-hidden="true"><rect x="4" y="1" width="8" height="14" rx="1.5" fill="none" stroke="var(--yellow)" stroke-width="2"/><rect x="6" y="3" width="4" height="7" fill="var(--yellow)"/></svg>
        604 873 1196
      </li>
      <li>
        <svg viewBox="0 0 16 16" aria-hidden="true"><rect x="1" y="3" width="14" height="10" fill="var(--blue)"/><path d="M1 3l7 6 7-6" fill="none" stroke="#fff" stroke-width="1.4"/></svg>
        yourname@harborlineframe.ca
      </li>
      <li>
        <svg viewBox="0 0 16 16" aria-hidden="true"><circle cx="8" cy="8" r="6.5" fill="none" stroke="var(--red)" stroke-width="1.6"/><path d="M1.5 8h13M8 1.5c-3 3-3 10 0 13M8 1.5c3 3 3 10 0 13" fill="none" stroke="var(--red)" stroke-width="1.2"/></svg>
        www.harborlineframe.ca
      </li>
    </ul>

    <div class="address">
      <p class="address-company">Harborline Frame Construction</p>
      <p class="address-line">Name of Street, Road, City, CA 3984</p>
    </div>

    <div class="pattern-band" role="img" aria-label="Decorative strip of coloured tilted blocks"></div>
  </section>

</main>
</body>
</html>
```